Stylish Business Cards Wanted

- DOUBLE SIDED Design Required -

High end, edgy cards for a corporate and personal stylist. Must include logo,
Name: Belinda Forsey
Title: Director and Stylist
telephone : +61 8 8217 4592
email: belinda@thegarbledger.example
website: thegarbledger.example
Tag: Corporate Workwear & Uniform Specialist | Personal Stylist
Would like nice icons for telephone, email, website

Target Market(s)

Businesses wanting stylish uniforms, people wanting stylish wardrobes

Industry/Entity Type

Corporate Workwear Stylist

Contact Information for Business Card

I would like black, white and gold foiling incorporated in the design - possibly a touch of the other colours on my branding guide attached Name: Belinda Forsey Title: Director and Stylist telephone : +61 8 8217 4592 email: belinda@thegarbledger.example website: thegarbledger.example Tag: Corporate Workwear & Uniform Specialist | Personal Stylist Would like nice icons for telephone, email, website

Font styles to use
Other font styles liked:
• Raleway

Colors

Designer to choose colors to be used in the design.

Requirements
Must have
• Gold foil accents

```html
<!DOCTYPE html>
<html lang="en">
<head>
<meta charset="utf-8">
<title>The Garb Ledger — Business Card</title>
<link href="https://fonts.googleapis.com/css2?family=Montserrat:wght@500;600;700&family=Raleway:wght@400;500;600&display=swap" rel="stylesheet">
<style>
  :root {
    --backdrop: #dcdcdc;
    --black: #0b0b0b;
    --white: #ffffff;
    --gold: #e8bf5a;
    --gold-deep: #d9aa3f;
    --ink: #1a1a1a;
  }
  * { box-sizing: border-box; margin: 0; padding: 0; }
  html, body {
    width: 1200px; height: 900px; overflow: hidden;
    background: var(--backdrop);
  }
  .canvas { position: relative; width: 1200px; height: 900px; }

  .card {
    position: absolute; left: 250px; width: 700px; height: 400px;
    overflow: hidden;
    box-shadow: 0 10px 24px rgba(0,0,0,0.22);
  }

  /* Front */
  .card-front { top: 35px; background: var(--black); }
  .front-band {
    position: absolute; left: 0; right: 0; bottom: 0; height: 135px;
    background: linear-gradient(100deg, var(--gold-deep), var(--gold) 55%, var(--gold-deep));
  }
  .front-name {
    position: absolute; left: 0; right: 0; top: 0; height: 265px;
    display: flex; align-items: center; justify-content: center;
    font-family: "Montserrat", sans-serif; font-weight: 600;
    font-size: 66px; letter-spacing: 2px; color: var(--gold);
  }

  /* Back */
  .card-back { top: 470px; background: var(--white); }
  .back-name {
    position: absolute; left: 0; top: 60px; width: 300px; height: 210px;
    display: flex; align-items: center; justify-content: center;
    font-family: "Montserrat", sans-serif; font-weight: 600;
    font-size: 30px; color: var(--black);
  }
  .divider {
    position: absolute; left: 318px; top: 60px; width: 2px; height: 215px;
    background: var(--gold);
  }
  .person { position: absolute; left: 350px; top: 68px; }
  .person-name {
    font-family: "Raleway", sans-serif; font-weight: 600;
    font-size: 27px; color: var(--ink);
  }
  .person-title {
    font-family: "Raleway", sans-serif; font-weight: 500;
    font-size: 14px; color: var(--gold); margin-top: 2px;
  }
  .contacts {
    position: absolute; left: 350px; top: 152px; list-style: none;
  }
  .contact {
    display: flex; align-items: center; gap: 14px;
    height: 32px;
    font-family: "Raleway", sans-serif; font-weight: 500;
    font-size: 17px; color: var(--ink);
  }
  .contact-icon { width: 22px; height: 22px; flex: none; }

  .rule-gold {
    position: absolute; left: 0; right: 0; top: 300px; height: 3px;
    background: var(--gold);
  }
  .tag-band {
    position: absolute; left: 0; right: 0; top: 315px; bottom: 0;
    background: var(--black);
    display: flex; flex-direction: column; align-items: center; justify-content: center;
    font-family: "Montserrat", sans-serif; font-weight: 500;
    font-size: 19px; letter-spacing: 0.5px; line-height: 1.35;
    color: var(--gold); text-transform: uppercase;
  }
  .tag-sep { margin: 0 10px; }
</style>
</head>
<body>
<main class="canvas">
  <section class="card card-front" aria-label="Card front">
    <div class="front-name">The Garb Ledger</div>
    <div class="front-band"></div>
  </section>

  <section class="card card-back" aria-label="Card back">
    <div class="back-name">The Garb Ledger</div>
    <div class="divider"></div>

    <div class="person">
      <p class="person-name">Belinda Forsey</p>
      <p class="person-title">Director and Stylist</p>
    </div>

    <ul class="contacts">
      <li class="contact">
        <svg class="contact-icon" viewBox="0 0 22 22" aria-hidden="true">
          <circle cx="11" cy="11" r="11" fill="#0b0b0b"/>
          <path d="M7.6 6.2l1.6-.4 1 2.4-1 .8c.5 1.2 1.5 2.2 2.7 2.8l.8-1 2.4 1-.4 1.6c-.2.5-.7.8-1.2.7C10.4 13.7 8.3 11.6 7 8.5c-.2-.6 0-1.1.6-1.3z" fill="#e8bf5a"/>
        </svg>
        <span>+61 8 8217 4592</span>
      </li>
      <li class="contact">
        <svg class="contact-icon" viewBox="0 0 22 22" aria-hidden="true">
          <circle cx="11" cy="11" r="11" fill="#0b0b0b"/>
          <rect x="5.5" y="7.5" width="11" height="7.5" fill="none" stroke="#e8bf5a" stroke-width="1.3"/>
          <path d="M5.5 7.5l5.5 4.3 5.5-4.3" fill="none" stroke="#e8bf5a" stroke-width="1.3"/>
        </svg>
        <span>belinda@thegarbledger.example</span>
      </li>
      <li class="contact">
        <svg class="contact-icon" viewBox="0 0 22 22" aria-hidden="true">
          <circle cx="11" cy="11" r="11" fill="#0b0b0b"/>
          <circle cx="11" cy="11" r="5.5" fill="none" stroke="#e8bf5a" stroke-width="1.2"/>
          <ellipse cx="11" cy="11" rx="2.4" ry="5.5" fill="none" stroke="#e8bf5a" stroke-width="1.1"/>
          <path d="M5.5 11h11" stroke="#e8bf5a" stroke-width="1.1"/>
        </svg>
        <span>www.thegarbledger.example</span>
      </li>
    </ul>

    <div class="rule-gold"></div>
    <div class="tag-band">
      <p>Corporate Workwear</p>
      <p>Uniform Specialist<span class="tag-sep">|</span>Personal Stylist</p>
    </div>
  </section>
</main>
</body>
</html>
```